Broschüre für Immobilienvertrieb
Zielgruppe
Wir sind ein Immobilienvertrieb im Bereich Neubau-Immobilien und Bestand-Immobilien aus München. Die Firma BLOR existiert seit über 30 Jahren. Vor 4 Jahren haben wir ein cooles modernes Rebranding durchgeführt, sodass man mit unserem neuen Corporate Design richtig Spaß am Gestalten haben kann.
Eine konkrete Zielgruppe zu definieren ist schwierig, da unsere Käufer von 20-80 Jahren sein können. Ob junge, erfolgreiche Menschen, junge Familien, ältere Erwachsene, die von sich nach Auszug ihrer Kinder von ihrem Haus trennen wollen und eine kleinere Wohnung suchen oder einfach der Kapitalanleger, der auf der Suche nach einer neuen Investition ist.
Unsere CI ist gradlinig und setzt sich aus anthrazit, neonorange und weiß zusammen (Styleguide ist anbei).
Im Bestand gibt es nicht pro Objekt ein CI, hier wird mit dem der BLOR gearbeitet. Im Neubau hat jedes einzelne Projekt sein eigenes CI (siehe aktuell hausfeld-neu.de).
www.blor.de
Aufgabenstellung
Zur Aufgabe: Für die Bestandimmobilien benötigen wir ein neues Layout eines Immobilienexposé. Das Exposé wird sowohl online verwendet als auch von uns selbst gedruckt und gebunden.
Input: beigefügt ein Beispielexposé - grundsätzlich gefällt uns das Design, wir möchten jedoch etwas NEUES, modernes. Bitte keine Kopien des alten Exposés, dies soll nur als Input dienen (gerne können die Daten der Wohnung für den neuen Designentwurf genutzt werden).
Die Datei soll von uns befüllbar sein, sodass wir Texte und Bilder selbst austauschen können.
Für die Onlinenutzung gerne als doppelseitige Datei, zum Beispiel um Bilder über zwei Seiten größer und schöner darstellen zu können (Auszug Beispielimmobilie anbei). Für den Druck wird die Datei zudem mit Einzelseiten benötigt.

```html
<!DOCTYPE html>
<html lang="de">
<head>
<meta charset="utf-8">
<title>BLOR Exposé – Lindenstraße München</title>
<link rel="stylesheet" href="https://fonts.googleapis.com/css2?family=Montserrat:wght@300;400;500;600;700&display=swap">
<style>
  :root {
    --neon-orange: #ea4a2a;
    --orange-light: #f08a4e;
    --anthracite: #2f3034;
    --white: #ffffff;
    --ink: #2b2b2b;
    --stage: #e8e6e3;
    --sky-top: #7d8fa0;
    --sky-low: #d5dadf;
  }
  * { margin: 0; padding: 0; box-sizing: border-box; }
  html, body {
    width: 1200px; height: 900px; overflow: hidden;
    background: var(--stage);
    font-family: "Montserrat", Arial, sans-serif;
  }

  /* ---------- Cover ---------- */
  .cover {
    position: absolute; left: 40px; top: 190px;
    width: 370px; height: 519px;
    overflow: hidden;
    box-shadow: 0 6px 18px rgba(0,0,0,.18);
  }
  .cover__photo {
    position: absolute; inset: 0;
    background: linear-gradient(160deg, #e4683c 0%, #ef8a4f 40%, #e8703f 70%, #d9552f 100%);
  }
  .cover__band {
    position: absolute; left: 0; right: 0; top: 370px; bottom: 0;
    background: var(--anthracite);
  }
  .cover__frame { position: absolute; inset: 0; }
  .brand {
    position: absolute; left: 0; right: 0; top: 62px;
    display: flex; justify-content: center; align-items: center; gap: 10px;
    color: var(--white);
  }
  .brand__square { width: 14px; height: 14px; border: 2px solid var(--white); }
  .brand__name { font-weight: 500; font-size: 30px; letter-spacing: 6px; }
  .cover__tagline {
    position: absolute; left: 0; right: 0; top: 119px;
    text-align: center; color: var(--white);
    font-weight: 600; font-size: 8.5px; letter-spacing: 1.8px;
  }
  .cover__title {
    position: absolute; left: 0; right: 0; top: 398px;
    text-align: center; color: var(--white);
    font-weight: 600; font-size: 15px; letter-spacing: 2.6px; line-height: 18px;
  }
  .cover__subtitle {
    position: absolute; left: 0; right: 0; top: 443px;
    text-align: center; color: #e6e6e6;
    font-weight: 400; font-size: 8.4px; letter-spacing: 1px; line-height: 11px;
  }
  .cover__object {
    position: absolute; left: 18px; top: 492px;
    color: var(--white); font-weight: 600; font-size: 6.8px; letter-spacing: 1.1px;
    white-space: nowrap;
  }

  /* ---------- Spread ---------- */
  .spread {
    position: absolute; left: 430px; top: 190px;
    width: 730px; height: 519px;
    background: var(--white);
    box-shadow: 0 6px 18px rgba(0,0,0,.18);
  }
  .spread__gutter {
    position: absolute; left: 364px; top: 0; width: 2px; height: 35px;
    background: linear-gradient(to right, rgba(0,0,0,.06), rgba(0,0,0,0));
  }
  .page-number {
    position: absolute; top: 20px;
    display: flex; align-items: center; gap: 6px;
    font-size: 5.5px; font-weight: 600; color: var(--ink);
  }
  .page-number__mark { width: 11px; height: 4px; background: var(--neon-orange); }
  .page-number--left { left: 4px; }
  .page-number--right { right: 4px; flex-direction: row-reverse; }
  .spread__photo {
    position: absolute; left: 20px; top: 35px; width: 690px; height: 448px;
    background: linear-gradient(100deg, var(--sky-top) 0%, var(--sky-low) 45%, #d9b89a 65%, #e2704a 85%, #c9522f 100%);
  }
  .headline {
    position: absolute; left: 88px; top: 207px;
    font-size: 15px; letter-spacing: 1.6px; line-height: 18px;
  }
  .headline__light { display: block; color: var(--white); font-weight: 300; }
  .headline__strong { display: block; color: var(--neon-orange); font-weight: 700; letter-spacing: 2px; }
  .page-footer {
    position: absolute; top: 495px; width: 365px;
    text-align: center; font-size: 5.3px; color: var(--ink);
  }
  .page-footer b { font-weight: 700; }
  .page-footer--left { left: 0; }
  .page-footer--right { left: 365px; }
</style>
</head>
<body>

<section class="cover">
  <div class="cover__photo" role="img" aria-label="Fassade eines Hochhauses mit Balkonen, in Orange eingefärbt"></div>
  <div class="cover__band"></div>
  <svg class="cover__frame" width="370" height="519" viewBox="0 0 370 519">
    <g stroke="#ffffff" stroke-width="2" fill="none">
      <line x1="18" y1="19" x2="263" y2="19"/>
      <line x1="18" y1="18" x2="18" y2="485"/>
      <line x1="350" y1="22" x2="350" y2="497"/>
      <line x1="110" y1="497" x2="351" y2="497"/>
    </g>
  </svg>
  <div class="brand">
    <span class="brand__square"></span>
    <span class="brand__name">BLOR</span>
  </div>
  <p class="cover__tagline">RAUM FÜR NEUE KAPITEL</p>
  <h1 class="cover__title">LINDENSTRASSE<br>MÜNCHEN</h1>
  <p class="cover__subtitle">MÖBILIERTE &amp; GUT VERMIETETE KAPITALANLAGE<br>IN GUTER LAGE MIT BALKON &amp; STELLPLATZ</p>
  <p class="cover__object">OBJEKT XX - 2.OG</p>
</section>

<section class="spread">
  <div class="spread__gutter"></div>
  <div class="page-number page-number--left"><span class="page-number__mark"></span><span>12</span></div>
  <div class="page-number page-number--right"><span class="page-number__mark"></span><span>13</span></div>
  <div class="spread__photo" role="img" aria-label="Untersicht eines Wohnhochhauses mit orangefarbenen Balkonträgern vor bewölktem Himmel"></div>
  <h2 class="headline">
    <span class="headline__light">AUS LIEBE ZUM</span>
    <span class="headline__strong">BESTEHENDEN</span>
  </h2>
  <p class="page-footer page-footer--left"><b>Exposé</b> | Lindenstr. 118 | Objektnr. XX - München</p>
  <p class="page-footer page-footer--right"><b>Exposé</b> | Lindenstr. 118 | Objektnr. XX - München</p>
</section>

</body>
</html>
```